Motor Vault Website - Part of the Brantley Group

A complimentary website is required for the launch of a 'Motor Vault' - a new service launched by industry renowned BRANTLEY. Motor Vault is an industry-first brand that designs and builds unique subterranean car parks for private residential homes in London and the influential counties within the UK. Please see here the direction of a new BRANTLEY Website - we would like Motor Vault to be complimentary and sit alongside BRANTLEY harmoniously - https://www.brantleyhomes.example/brantley-nu-staging Brantley have some images, but whilst more professional images are in production - we have also attached pixmora photos- named clearly as pixmora. **Attached files include JPEG, .eps of logo and Brantley library images and Pixmora Library Images - two versions of logo dependent on background colour. - Website needs to be sleek, chic and masculine.- Colour Palette - Grey/ Black/ White - Same visiual journey as Brantley website- Required areas within the sit include - About Us / Our Work / Contact Page

Target Market(s)

Luxury
Men

Number of Pages Required

2 page

Font styles to use
Sans Serif

Colors
e8e8e8
757575
1b1b1b
000000
9d9d9d
cbcbcb
f5f5f5

Requirements
Must have
• Complimentary of this site - https://www.brantleyhomes.example/brantley-nu-staging
Should not have
• Colour

```html
<!DOCTYPE html>
<html lang="en">
<head>
<meta charset="utf-8">
<title>Motor Vault — Part of the Brantley Group</title>
<link href="https://fonts.googleapis.com/css2?family=Libre+Baskerville&family=Montserrat:wght@400;500;600;700&family=Open+Sans:wght@400;600&display=swap" rel="stylesheet">
<style>
:root{
  --white:#ffffff;
  --off:#f5f5f5;
  --light:#e8e8e8;
  --silver:#cbcbcb;
  --mid:#9d9d9d;
  --grey:#757575;
  --dark:#1b1b1b;
  --black:#000000;
  --serif:'Libre Baskerville', Georgia, serif;
  --sans:'Montserrat', Arial, sans-serif;
  --body:'Open Sans', Arial, sans-serif;
}
*{margin:0;padding:0;box-sizing:border-box}
html,body{width:1200px;height:4150px;overflow:hidden}
body{position:relative;background:var(--white);font-family:var(--body);color:var(--dark)}
.abs{position:absolute}
.photo{position:absolute}

/* navigation */
.site-nav{position:absolute;left:0;top:0;width:1200px;height:75px;background:var(--white);display:flex;align-items:center;justify-content:space-between;padding:0 60px 0 28px}
.brand{font-family:var(--sans);font-weight:700;letter-spacing:1px;color:var(--dark);display:flex;align-items:center;gap:8px;font-size:24px}
.brand-mark{width:16px;height:16px;background:currentColor}
.nav-links{display:flex;gap:30px;list-style:none;font-family:var(--sans);font-size:12px;letter-spacing:1px;color:var(--grey)}
.nav-links .active{color:var(--dark);font-weight:600}

/* hero */
.hero{left:0;top:75px;width:1200px;height:615px;background:radial-gradient(ellipse at 50% 35%,#5a5a5a 0%,#2c2c2c 45%,#0d0d0d 100%)}
.hero-logo{position:absolute;left:310px;top:300px;width:580px;text-align:center;color:var(--white)}
.hero-logo .brand{color:var(--white);font-size:66px;justify-content:center;gap:16px}
.hero-logo .brand-mark{width:44px;height:44px}
.hero-tag{font-family:var(--sans);font-size:13px;letter-spacing:1px;text-align:right;margin-top:4px;color:var(--silver)}
.hero-down{position:absolute;left:588px;top:625px}

/* shared type */
.eyebrow{position:absolute;font-family:var(--sans);font-size:15px;letter-spacing:1px;color:var(--grey);display:flex;align-items:center;gap:18px}
.eyebrow::after{content:"";width:90px;height:1px;background:var(--grey)}
.heading{position:absolute;font-family:var(--serif);font-size:27px;line-height:1.25;letter-spacing:1px;color:var(--dark);text-transform:uppercase}
.copy{position:absolute;font-size:13px;line-height:1.55;color:var(--grey)}
.more{position:absolute;font-family:var(--sans);font-size:12px;font-weight:600;letter-spacing:1px;color:var(--dark);display:flex;align-items:center;gap:10px}
.arrow-btn{position:absolute;width:45px;height:45px;background:var(--black);display:flex;align-items:center;justify-content:center}

/* intro */
.intro-title{left:0;width:1200px;top:770px;text-align:center;font-family:var(--serif);font-size:22px;letter-spacing:2px;color:var(--dark)}
.intro-copy{left:230px;width:740px;top:815px;text-align:center;font-size:13px;line-height:1.6;color:var(--mid)}

/* projects */
.projects{left:0;top:1650px;width:1200px;height:760px;background:linear-gradient(135deg,var(--off),#ececec 50%,var(--off))}
.project-caption{position:absolute;left:203px;top:2070px;width:380px;color:var(--white)}
.project-caption h3{font-family:var(--serif);font-size:20px;line-height:1.3;text-transform:uppercase;letter-spacing:1px}
.project-caption p{font-size:13px;line-height:1.5;color:var(--silver);margin-top:14px}
.project-caption .more{position:static;color:var(--white);margin-top:20px}

/* contact */
.contact-panel{left:28px;top:3050px;width:1144px;height:667px;background:radial-gradient(ellipse at 55% 45%,#3a3a3a 0%,#1a1a1a 55%,#050505 100%)}
.contact-content{position:absolute;left:28px;top:3050px;width:1144px;height:667px}
.contact-content .eyebrow{color:var(--white)}
.contact-content .eyebrow::after{background:var(--white)}
.contact-content .heading{color:var(--white)}
.contact-content .copy{color:var(--silver)}
.contact-line{position:absolute;display:flex;align-items:center;gap:14px;font-size:12px;color:var(--silver);font-family:var(--sans)}
.field{position:absolute;background:rgba(120,120,120,.45);color:var(--silver);font-size:12px;padding:12px 14px;font-family:var(--body)}
.submit{position:absolute;left:612px;top:3617px;width:415px;height:38px;background:var(--black);color:var(--white);font-family:var(--sans);font-size:12px;font-weight:600;letter-spacing:1px;display:flex;align-items:center;justify-content:center}

/* footer */
.site-footer{position:absolute;left:0;top:3759px;width:1200px;height:391px;background:var(--dark);color:var(--white);text-align:center}
.site-footer .brand{color:var(--white);justify-content:center;margin-top:72px;font-size:34px;gap:12px}
.site-footer .brand-mark{width:22px;height:22px}
.footer-tag{font-family:var(--sans);font-size:9px;color:var(--mid);letter-spacing:1px;margin-top:2px}
.social{display:flex;justify-content:center;gap:20px;margin-top:60px}
.social span{width:40px;height:40px;border:1px solid var(--grey);border-radius:50%}
.footer-links{display:flex;justify-content:center;gap:22px;list-style:none;font-family:var(--sans);font-size:10px;color:var(--silver);margin-top:34px;letter-spacing:1px}
.copyright{font-family:var(--sans);font-size:9px;color:var(--grey);margin-top:14px;letter-spacing:1px}
</style>
</head>
<body>

<header class="site-nav">
  <div class="brand"><span class="brand-mark"></span>MOTOR VAULT</div>
  <ul class="nav-links">
    <li class="active">HOME</li><li>ABOUT US</li><li>OUR WORK</li><li>CONTACT US</li>
  </ul>
</header>

<section>
  <div class="photo hero" role="img" aria-label="Dark concrete underground car park lit by ceiling lights"></div>
  <div class="hero-logo">
    <div class="brand"><span class="brand-mark"></span>MOTOR VAULT</div>
    <div class="hero-tag">PART OF THE BRANTLEY GROUP</div>
  </div>
  <svg class="hero-down" width="24" height="34" viewBox="0 0 24 34"><path d="M12 2v28M4 22l8 8 8-8" stroke="#fff" stroke-width="2" fill="none"/></svg>
</section>

<section>
  <h1 class="abs intro-title">DESIGNS AND BUILDS UNIQUE SUBTERRANEAN CAR PARKS</h1>
  <p class="abs intro-copy">Motor Vault is an industry-first brand that designs and builds unique subterranean car parks for private residential homes in London and the influential counties within the UK.</p>
</section>

<section>
  <div class="eyebrow" style="left:170px;top:917px">SERVICES</div>
  <h2 class="heading" style="left:170px;top:962px">Our Professional<br>Specializations</h2>
  <div class="photo" style="left:173px;top:1075px;width:415px;height:320px;background:linear-gradient(160deg,#8a8a8a,#2e2e2e 60%,#111)" role="img" aria-label="Steel reinforcement framework during excavation"></div>
  <div class="photo" style="left:612px;top:1075px;width:415px;height:320px;background:linear-gradient(200deg,#777,#303030 55%,#0e0e0e)" role="img" aria-label="Worker welding steel with sparks on site"></div>
  <div class="arrow-btn" style="left:76px;top:1212px"><svg width="16" height="12" viewBox="0 0 16 12"><path d="M15 6H2M6 1L1 6l5 5" stroke="#fff" stroke-width="1.5" fill="none"/></svg></div>
  <div class="arrow-btn" style="left:1080px;top:1212px"><svg width="16" height="12" viewBox="0 0 16 12"><path d="M1 6h13M10 1l5 5-5 5" stroke="#fff" stroke-width="1.5" fill="none"/></svg></div>

  <h3 class="abs" style="left:173px;top:1432px;font-family:var(--serif);font-size:17px;letter-spacing:1px">DESIGN</h3>
  <p class="copy" style="left:173px;top:1470px;width:415px">Excepteur sint occaecat cupidatat non proident sunt in culpa qui officia deserunt mollit anim id est laborum. Duis aute irure in voluptate.</p>
  <div class="more" style="left:173px;top:1560px">READ MORE <svg width="16" height="10" viewBox="0 0 16 10"><path d="M1 5h13M10 1l4 4-4 4" stroke="#1b1b1b" stroke-width="1.5" fill="none"/></svg></div>

  <h3 class="abs" style="left:612px;top:1432px;font-family:var(--serif);font-size:17px;letter-spacing:1px">DEVELOPMENT</h3>
  <p class="copy" style="left:612px;top:1470px;width:415px">Excepteur sint occaecat cupidatat non proident sunt in culpa qui officia deserunt mollit anim id est laborum. Duis aute irure in voluptate.</p>
  <div class="more" style="left:612px;top:1560px">READ MORE <svg width="16" height="10" viewBox="0 0 16 10"><path d="M1 5h13M10 1l4 4-4 4" stroke="#1b1b1b" stroke-width="1.5" fill="none"/></svg></div>
</section>

<section>
  <div class="abs projects"></div>
  <div class="eyebrow" style="left:170px;top:1720px">PROJECTS</div>
  <h2 class="heading" style="left:170px;top:1775px">Explore Motor Vault<br>Projects</h2>
  <div class="photo" style="left:173px;top:1888px;width:854px;height:387px;background:linear-gradient(100deg,#0a0a0a 0%,#2a2a2a 40%,#5e5e5e 70%,#1c1c1c 100%)" role="img" aria-label="Underground car park under construction with steel mesh walls"></div>
  <div class="arrow-btn" style="left:140px;top:2048px;width:41px;height:41px"><svg width="14" height="12" viewBox="0 0 16 12"><path d="M15 6H2M6 1L1 6l5 5" stroke="#fff" stroke-width="1.5" fill="none"/></svg></div>
  <div class="arrow-btn" style="left:1010px;top:2048px;width:41px;height:41px"><svg width="14" height="12" viewBox="0 0 16 12"><path d="M1 6h13M10 1l5 5-5 5" stroke="#fff" stroke-width="1.5" fill="none"/></svg></div>
  <div class="project-caption">
    <h3>Similique sunt in culpa qui officia deserunt</h3>
    <p>Nam libero tempore cum soluta nobis est eligendi optio cumque nihil impedit quo minus id quod maxime placeat facere possimus.</p>
    <div class="more">READ MORE <svg width="16" height="10" viewBox="0 0 16 10"><path d="M1 5h13M10 1l4 4-4 4" stroke="#fff" stroke-width="1.5" fill="none"/></svg></div>
  </div>
  <div class="more" style="left:550px;top:2330px">VIEW ALL <svg width="16" height="10" viewBox="0 0 16 10"><path d="M1 5h13M10 1l4 4-4 4" stroke="#1b1b1b" stroke-width="1.5" fill="none"/></svg></div>
</section>

<section>
  <div class="photo" style="left:173px;top:2510px;width:418px;height:436px;background:radial-gradient(circle at 62% 30%,#d8d8d8 0%,#6a6a6a 25%,#222 60%,#0a0a0a 100%)" role="img" aria-label="Light shining into a concrete underground chamber"></div>
  <div class="abs" style="left:173px;top:2898px;width:48px;height:48px;background:var(--silver);display:flex;align-items:center;justify-content:center"><svg width="16" height="12" viewBox="0 0 16 12"><path d="M15 6H2M6 1L1 6l5 5" stroke="#1b1b1b" stroke-width="1.5" fill="none"/></svg></div>
  <div class="abs" style="left:221px;top:2898px;width:48px;height:48px;background:var(--mid);display:flex;align-items:center;justify-content:center"><svg width="16" height="12" viewBox="0 0 16 12"><path d="M1 6h13M10 1l5 5-5 5" stroke="#1b1b1b" stroke-width="1.5" fill="none"/></svg></div>
  <div class="eyebrow" style="left:612px;top:2584px">ABOUT US</div>
  <h2 class="heading" style="left:612px;top:2643px">An Industry-First<br>Brand</h2>
  <p class="copy" style="left:612px;top:2730px;width:415px">Neque porro quisquam est qui dolorem ipsum quia dolor sit amet consectetur adipisci velit sed quia non numquam eius modi tempora incidunt ut labore et dolore magnam.</p>
  <div class="more" style="left:612px;top:2835px">READ MORE <svg width="16" height="10" viewBox="0 0 16 10"><path d="M1 5h13M10 1l4 4-4 4" stroke="#1b1b1b" stroke-width="1.5" fill="none"/></svg></div>
</section>

<section>
  <div class="photo contact-panel" role="img" aria-label="Dark concrete basement corridor with columns"></div>
  <div class="contact-content">
    <div class="eyebrow" style="left:145px;top:125px">CONTACT US</div>
    <h2 class="heading" style="left:145px;top:172px">Let's Start New<br>Projects</h2>
    <p class="copy" style="left:145px;top:307px;width:400px">Nam libero tempore cum soluta nobis est eligendi optio cumque nihil impedit quo minus id quod maxime placeat facere possimus omnis voluptas assumenda est omnis dolor repellendus.</p>
    <div class="contact-line" style="left:145px;top:460px"><svg width="12" height="16" viewBox="0 0 12 16"><path d="M6 15S1 9 1 6a5 5 0 0 1 10 0c0 3-5 9-5 9z" fill="#cbcbcb"/><circle cx="6" cy="6" r="2" fill="#1b1b1b"/></svg>12 HARLOW MEWS, LONDON, W1 4QX</div>
    <div class="contact-line" style="left:145px;top:495px"><svg width="13" height="13" viewBox="0 0 13 13"><path d="M3 1l2 3-1.5 1.5a7 7 0 0 0 4 4L9 8l3 2-1 2c-5 0-10-5-10-10z" fill="#cbcbcb"/></svg>0207 555 0148</div>
  </div>
  <div class="field" style="left:612px;top:3368px;width:415px;height:38px">Name</div>
  <div class="field" style="left:612px;top:3420px;width:203px;height:38px">Email</div>
  <div class="field" style="left:824px;top:3420px;width:203px;height:38px">Phone</div>
  <div class="field" style="left:612px;top:3472px;width:415px;height:130px">Message</div>
  <div class="submit">SUBMIT</div>
</section>

<footer class="site-footer">
  <div class="brand"><span class="brand-mark"></span>MOTOR VAULT</div>
  <div class="footer-tag">PART OF THE BRANTLEY GROUP</div>
  <div class="social"><span></span><span></span><span></span><span></span></div>
  <ul class="footer-links"><li>HOME</li><li>ABOUT US</li><li>OUR WORK</li><li>CONTACT US</li></ul>
  <div class="copyright">COPYRIGHT INFORMATION HERE</div>
</footer>

</body>
</html>
```